Christmas Collection Candle Label Design

Looking to update our existing Christmas Candle Collection labels. Labels should reflect the overall feel of our brand- www.wickmerelane.ca
Want to include some color elements. Holiday colors added into design but more muted/ earthy tones not vibrant colors . Metallic elements and line art botanical illustration. Fonts should be more align to brand
Scents
Holiday Tree
Candy Cane
Sugar and Spice
Joyeaux Noel

```html
<!DOCTYPE html>
<html lang="en">
<head>
<meta charset="utf-8">
<title>Christmas Candle Design – Wickmere Lane</title>
<link rel="stylesheet" href="https://fonts.googleapis.com/css2?family=Josefin+Sans:wght@600&family=Marcellus&family=Mrs+Saint+Delafield&display=swap">
<style>
  :root {
    --page-bg: #f4f4f4;
    --label-bg: #ffffff;
    --ink: #1d1d1d;
    --gold: #c9a227;
    --gold-light: #f5dc74;
    --gold-deep: #b8901c;
    --red: #a3161d;
    --red-light: #e8474d;
    --red-deep: #b81a24;
    --green: #4f7a55;
    --green-light: #0d7a4a;
    --green-deep: #053a22;
    --copper: #c46a35;
    --copper-light: #fcc08a;
    --copper-deep: #8d4520;
  }
  * { margin: 0; padding: 0; box-sizing: border-box; }
  html, body {
    width: 720px;
    height: 1200px;
    overflow: hidden;
    background: var(--page-bg);
  }
  .sheet {
    position: relative;
    width: 720px;
    height: 1200px;
  }
  .sheet-title {
    position: absolute;
    top: 176px;
    left: 0;
    width: 720px;
    text-align: center;
    font-family: "Josefin Sans", sans-serif;
    font-weight: 600;
    font-size: 15px;
    letter-spacing: 4.5px;
    color: var(--ink);
  }
  .label {
    position: absolute;
    width: 330px;
    height: 326px;
    background: var(--label-bg);
    overflow: hidden;
  }
  .label--noel   { left: 12px;  top: 250px; --accent: var(--gold); }
  .label--candy  { left: 356px; top: 250px; --accent: var(--red); }
  .label--tree   { left: 34px;  top: 620px; --accent: var(--green); }
  .label--spice  { left: 378px; top: 620px; --accent: var(--copper); }

  .label__brand {
    position: absolute;
    left: 33px;
    top: 84px;
    font-family: "Marcellus", serif;
    font-size: 10px;
    letter-spacing: 1.6px;
    color: var(--ink);
  }
  .label__name {
    position: absolute;
    left: 33px;
    top: 120px;
    font-family: "Marcellus", serif;
    font-size: 29px;
    letter-spacing: 3.4px;
    line-height: 1;
    color: var(--ink);
  }
  .label__script {
    position: absolute;
    left: 33px;
    top: 146px;
    font-family: "Mrs Saint Delafield", cursive;
    font-size: 46px;
    line-height: 1;
    color: var(--ink);
  }
  .label__rule {
    position: absolute;
    left: 33px;
    top: 209px;
    width: 147px;
    height: 1.5px;
    background: var(--accent);
  }
  .label__facts {
    position: absolute;
    left: 33px;
    top: 234px;
    list-style: none;
    font-family: "Marcellus", serif;
    font-size: 10.5px;
    letter-spacing: 1.4px;
    line-height: 20px;
    color: var(--ink);
  }
  .label__art {
    position: absolute;
    right: 0;
    top: 0;
    width: 130px;
    height: 276px;
  }
  .label__band {
    position: absolute;
    left: 0;
    bottom: 0;
    width: 100%;
    height: 23px;
  }
  .label--noel .label__band {
    background: linear-gradient(90deg, var(--gold-deep), var(--gold-light) 35%, #e3b12a 55%, var(--gold-light) 72%, var(--gold-deep));
  }
  .label--candy .label__band {
    background: linear-gradient(90deg, var(--red-deep), var(--red-light) 30%, #d62c33 60%, var(--red-deep));
  }
  .label--tree .label__band {
    background: linear-gradient(90deg, #0a5a35, var(--green-light) 40%, #0b5c36 65%, var(--green-deep));
  }
  .label--spice .label__band {
    background: linear-gradient(90deg, #d08a5a, #a8531f 30%, var(--copper-light) 65%, var(--copper-deep));
  }
</style>
</head>
<body>
<main class="sheet">
  <h1 class="sheet-title">CHRISTMAS CANDLE DESIGN</h1>

  <section class="label label--noel">
    <p class="label__brand">WICKMERE LANE</p>
    <h2 class="label__name">JOYEAUX</h2>
    <p class="label__script">Neol</p>
    <div class="label__rule"></div>
    <ul class="label__facts">
      <li>NATURAL SOY</li>
      <li>NET WT. 10OZ/283G</li>
      <li>MADE IN CANADA</li>
    </ul>
    <svg class="label__art" viewBox="0 0 130 276" role="img" aria-label="Gold line-art botanical sprig with small sparkles">
      <defs>
        <radialGradient id="noel-art" cx="0.6" cy="0.45" r="0.6">
          <stop offset="0" stop-color="#c9a227" stop-opacity="0.22"/>
          <stop offset="1" stop-color="#c9a227" stop-opacity="0"/>
        </radialGradient>
      </defs>
      <rect width="130" height="276" fill="url(#noel-art)"/>
    </svg>
    <div class="label__band"></div>
  </section>

  <section class="label label--candy">
    <p class="label__brand">WICKMERE LANE</p>
    <h2 class="label__name">CANDY</h2>
    <p class="label__script">Cane</p>
    <div class="label__rule"></div>
    <ul class="label__facts">
      <li>NATURAL SOY</li>
      <li>NET WT. 10OZ/283G</li>
      <li>MADE IN CANADA</li>
    </ul>
    <svg class="label__art" viewBox="0 0 130 276" role="img" aria-label="Deep red snowflake illustrations with scattered dots">
      <defs>
        <radialGradient id="candy-art" cx="0.55" cy="0.45" r="0.6">
          <stop offset="0" stop-color="#a3161d" stop-opacity="0.2"/>
          <stop offset="1" stop-color="#a3161d" stop-opacity="0"/>
        </radialGradient>
      </defs>
      <rect width="130" height="276" fill="url(#candy-art)"/>
    </svg>
    <div class="label__band"></div>
  </section>

  <section class="label label--tree">
    <p class="label__brand">WICKMERE LANE</p>
    <h2 class="label__name">HOLIDAY</h2>
    <p class="label__script">Tree</p>
    <div class="label__rule"></div>
    <ul class="label__facts">
      <li>NATURAL SOY</li>
      <li>NET WT. 10OZ/283G</li>
      <li>MADE IN CANADA</li>
    </ul>
    <svg class="label__art" viewBox="0 0 130 276" role="img" aria-label="Green line-art pine branch with pine cone">
      <defs>
        <radialGradient id="tree-art" cx="0.6" cy="0.45" r="0.6">
          <stop offset="0" stop-color="#4f7a55" stop-opacity="0.22"/>
          <stop offset="1" stop-color="#4f7a55" stop-opacity="0"/>
        </radialGradient>
      </defs>
      <rect width="130" height="276" fill="url(#tree-art)"/>
    </svg>
    <div class="label__band"></div>
  </section>

  <section class="label label--spice">
    <p class="label__brand">WICKMERE LANE</p>
    <h2 class="label__name">SUGAR &amp;</h2>
    <p class="label__script">Spice</p>
    <div class="label__rule"></div>
    <ul class="label__facts">
      <li>NATURAL SOY</li>
      <li>NET WT. 10OZ/283G</li>
      <li>MADE IN CANADA</li>
    </ul>
    <svg class="label__art" viewBox="0 0 130 276" role="img" aria-label="Copper line-art leafy vine with cloves">
      <defs>
        <radialGradient id="spice-art" cx="0.6" cy="0.45" r="0.6">
          <stop offset="0" stop-color="#c46a35" stop-opacity="0.22"/>
          <stop offset="1" stop-color="#c46a35" stop-opacity="0"/>
        </radialGradient>
      </defs>
      <rect width="130" height="276" fill="url(#spice-art)"/>
    </svg>
    <div class="label__band"></div>
  </section>
</main>
</body>
</html>
```